Design a wordpress website for IT consulting firm

We are a fintech+blockchain+full stack + software development consulting team. We offer services in these areas, we would like to design a new wordpress website.

The winner would need to first come with the graphic design(how it looks) and then actually build the website in wordpress. Contestants will be judged based on their We want to aim for professional look, and also how modern it looks

*** we also might have the chance to work together in the future for both projects and upgrading this website, so it is a good opportunity to get to know each other.

We would need 5 pages:
1. landing page, scroll down page that tells customer what services we offer(full stack software development, website design, fintech, blockchain)
2. about us: place where we can post information about our team
3. services: tab that explain in detail about what we can offer ( there should be a sub page about fintech, web design, big data, blockchain and full stack development)
4. contact us: a contact page that

```html
<!DOCTYPE html>
<html lang="en">
<head>
<meta charset="utf-8">
<title>Northgate Tech Advisory</title>
<link href="https://fonts.googleapis.com/css2?family=Maven+Pro:wght@400;500;600;700&family=Montserrat:wght@700;800&family=Great+Vibes&family=Open+Sans:wght@400;600;700&family=Lora:ital,wght@1,400;1,700&display=swap" rel="stylesheet">
<style>
:root{
  --navy:#1f2b4d;
  --navy-deep:#18223f;
  --pink:#f2505f;
  --white:#ffffff;
  --ink:#2b3450;
  --muted:#8a8fa0;
  --line:#e6e7ec;
  --map:#efe6d6;
}
*{box-sizing:border-box;margin:0;padding:0}
html,body{width:1200px;height:4339px;overflow:hidden}
body{position:relative;background:var(--white);font-family:"Open Sans",sans-serif;color:var(--ink)}
.abs{position:absolute}
.heading{font-family:"Maven Pro",sans-serif;font-weight:600;color:var(--navy);font-size:36px;text-align:center;width:1200px;left:0}
.connector{position:absolute;left:600px;width:0;border-left:2px dotted #c9ccd6;height:44px}
.btn{position:absolute;background:var(--pink);color:var(--white);font-family:"Open Sans",sans-serif;font-weight:700;font-size:14px;display:flex;align-items:center;justify-content:center;gap:8px;letter-spacing:.3px}

/* top bar */
.topbar{left:0;top:0;width:1200px;height:40px;background:var(--navy)}
.topbar .social{left:112px;top:12px;display:flex;gap:14px}
.topbar .social span{width:14px;height:14px;border-radius:50%;background:var(--white);display:block}
.topbar .contact{right:112px;top:11px;color:var(--white);font-size:13px;display:flex;gap:24px;align-items:center}
.topbar .contact b{color:var(--pink);margin-right:6px}

/* hero */
.hero{left:0;top:40px;width:1200px;height:610px;background:linear-gradient(110deg,#c9d3e4 0%,#8e9fbe 35%,#3a4a70 60%,#1f2b4d 80%)}
.header-shape{left:0;top:40px;width:1200px;height:122px}
.brand{display:flex;align-items:center;gap:10px;font-family:"Maven Pro",sans-serif;font-weight:500;font-size:22px;line-height:26px;white-space:nowrap}
.brand .mark{width:14px;height:14px;background:currentColor;display:block;flex:none}
.logo{left:113px;top:86px;color:var(--navy)}
.nav{top:79px;right:113px;display:flex;align-items:center;gap:34px;font-size:13px;color:#5b6278}
.nav .enquiry{background:var(--pink);color:var(--white);font-weight:600;padding:8px 16px}
.hero-copy{right:113px;top:268px;text-align:right;padding-right:22px;border-right:1px solid var(--white);height:188px}
.hero-copy .script{font-family:"Great Vibes",cursive;font-size:54px;color:var(--pink);line-height:54px}
.hero-copy .big{font-family:"Montserrat",sans-serif;font-weight:800;font-size:58px;color:var(--white);line-height:60px;letter-spacing:1px}
.hero-dots{left:114px;top:382px;display:flex;flex-direction:column;gap:8px;align-items:center}
.hero-dots span{width:7px;height:7px;border-radius:50%;background:var(--white)}
.hero-dots span.on{width:12px;height:12px;border:2px solid var(--pink);background:transparent}

/* services */
.svc{position:absolute;top:893px;width:223px;height:293px;background:var(--navy);border-radius:14px}
.svc .bubble{position:absolute;left:24px;top:0;width:175px;height:160px;background:var(--white);border-radius:0 0 14px 14px;box-shadow:0 4px 10px rgba(0,0,0,.08);padding:36px 10px 0;font-size:10.5px;line-height:18px;color:#a3a7b4;text-align:center}
.svc .bubble:after{content:"";position:absolute;left:78px;bottom:-14px;border:10px solid transparent;border-top:14px solid var(--white);border-bottom:0}
.svc .icon{position:absolute;left:85px;top:-26px;width:54px;height:50px;background:var(--white)}
.svc .label{position:absolute;left:14px;top:205px;display:flex;align-items:center;gap:12px;color:var(--white);font-family:"Maven Pro",sans-serif;font-weight:600;font-size:16px;line-height:20px}
.svc .label em{font-style:normal;font-weight:400;font-size:48px;line-height:48px}
.svc-shadow{position:absolute;top:1186px;width:223px;height:80px;background:linear-gradient(#eceef3,#ffffff)}

/* banner */
.banner{left:113px;top:1291px;width:974px;height:177px;border-radius:16px;background:linear-gradient(90deg,#1f2b4d 0%,#2c3a60 60%,#45557c 100%)}
.banner h3{position:absolute;left:75px;top:44px;font-family:"Maven Pro",sans-serif;font-weight:500;font-size:34px;color:var(--white)}
.banner p{position:absolute;left:75px;top:88px;font-family:"Maven Pro",sans-serif;font-size:23px;color:var(--white)}

/* projects */
.filters{left:256px;top:1643px;width:688px;height:42px;border-bottom:2px solid #f7b3ba;border-left:2px solid #f7b3ba;border-right:2px solid #f7b3ba;border-radius:0 0 12px 12px;display:flex;justify-content:center;gap:16px;font-size:12px;color:#9a9eab;padding-top:6px}
.filters span:before{content:"";display:inline-block;width:9px;height:9px;background:#c8cbd5;margin-right:5px;border-radius:2px}
.filters span:first-child:before{background:var(--pink)}
.photo{position:absolute}

/* testimonial */
.band{left:0;top:2474px;width:1200px;height:335px;background:var(--navy)}
.quote{left:585px;top:2518px;width:452px;font-family:"Lora",serif;font-style:italic;font-size:12.5px;line-height:21px;color:#d7dbe6}
.quote .who{margin-top:16px;font-weight:700;font-size:14px;color:var(--white);letter-spacing:.5px}
.quote .role{font-size:11px;color:#aab0c2}
.tdots{left:1080px;top:2620px;display:flex;flex-direction:column;gap:8px;align-items:center}
.tdots span{width:5px;height:5px;border-radius:50%;background:var(--white)}
.tdots span.on{width:8px;height:8px;background:transparent;border:1px solid var(--white)}

/* blog */
.lead{left:280px;top:2969px;width:640px;text-align:center;font-size:13px;line-height:20px;color:#56607a}
.post{position:absolute;top:3035px;width:300px}
.post .img{height:192px}
.post .date{position:absolute;left:0;top:192px;width:50px;height:54px;background:var(--pink);color:var(--white);font-family:"Maven Pro",sans-serif;font-size:16px;line-height:20px;padding:6px 0 0 12px}
.post .title{position:absolute;left:68px;top:203px;font-family:"Maven Pro",sans-serif;font-weight:600;font-size:12px;color:var(--navy);letter-spacing:.3px}
.post .meta{position:absolute;left:68px;top:226px;font-size:9px;color:#a0a4b0}
.post .excerpt{position:absolute;left:0;top:270px;width:300px;font-size:11.5px;line-height:20px;color:#6b7186}

/* contact */
.contact-info{left:303px;top:3513px;width:270px;height:366px;background:var(--navy);padding:42px 0 0 44px;color:var(--white)}
.contact-info h3{font-family:"Maven Pro",sans-serif;font-weight:500;font-size:32px;margin-bottom:30px}
.contact-info .row{display:flex;gap:12px;font-size:12px;line-height:18px;margin-bottom:18px}
.contact-info svg{flex:none;margin-top:2px}
.contact-form{left:573px;top:3513px;width:322px;height:366px;background:var(--white);padding:42px 22px 0}
.contact-form h3{font-family:"Maven Pro",sans-serif;font-weight:500;font-size:32px;color:var(--navy)}
.contact-form .sub{font-size:11px;color:#8a8fa0;margin:4px 0 14px}
.field{border-bottom:1px solid #f29ba4;height:44px;font-size:10px;font-style:italic;color:#b6b9c4;padding-top:14px;margin-bottom:2px}
.field.tall{height:58px}

/* footer */
.footer{left:0;top:3935px;width:1200px;height:404px;background:var(--navy);color:var(--white)}
.flogo{left:113px;top:4042px;color:var(--white)}
.fabout{left:113px;top:4106px;width:340px;font-size:10.5px;line-height:21px;color:#c3c8d6}
.fcol{top:4021px;font-size:11px;color:#c3c8d6}
.fcol h4{font-family:"Maven Pro",sans-serif;font-weight:600;font-size:17px;color:var(--white);margin-bottom:20px}
.fcol li{list-style:none;margin-bottom:19px}
.newsletter input{display:block;width:202px;height:34px;border:0;padding-left:10px;font-size:10px;font-style:italic;margin-bottom:10px}
.copy{left:113px;top:4281px;font-size:10px;color:#c3c8d6}
.fsocial{right:113px;top:4269px;display:flex;gap:8px}
.fsocial span{width:32px;height:32px;border-radius:50%;background:var(--pink);display:block}
</style>
</head>
<body>

<!-- top bar -->
<div class="abs topbar">
  <div class="abs social"><span></span><span></span><span></span><span></span><span></span></div>
  <div class="abs contact">
    <span><b>&#9990;</b>1800 555 0142</span>
    <span><b>&#9993;</b>hello@northgate.example</span>
  </div>
</div>

<!-- hero -->
<div class="abs hero" role="img" aria-label="Photo of a consulting team working around a white table with a laptop, seen from above"></div>
<svg class="abs header-shape" viewBox="0 0 1200 122" width="1200" height="122" aria-hidden="true">
  <path d="M0 0 H1200 V40 C1200 90 1150 92 1080 92 L150 96 C60 98 20 110 0 122 Z" fill="#ffffff"/>
</svg>
<div class="abs brand logo"><span class="mark"></span>Northgate Tech Advisory</div>
<nav class="abs nav">
  <span>About Us</span><span>Services</span><span>Contact Us</span>
  <span class="enquiry">FREE ENQUIRY</span>
</nav>
<div class="abs hero-dots"><span class="on"></span><span></span><span></span></div>
<div class="abs hero-copy">
  <div class="script">We are a</div>
  <div class="big">CONSULTING</div>
  <div class="big">TEAM</div>
</div>
<div class="btn" style="left:934px;top:489px;width:153px;height:42px;font-size:13px">Explore More &#8594;</div>
<svg class="abs" style="left:584px;top:604px" width="32" height="32" aria-hidden="true"><circle cx="16" cy="16" r="14" fill="none" stroke="#fff" stroke-width="1.5"/><path d="M10 14 L16 20 L22 14" fill="none" stroke="#fff" stroke-width="1.5"/></svg>

<!-- services -->
<div class="connector" style="top:676px"></div>
<h2 class="abs heading" style="top:726px">What Services We Offer</h2>

<div class="svc-shadow" style="left:113px"></div>
<div class="svc-shadow" style="left:362px"></div>
<div class="svc-shadow" style="left:612px"></div>
<div class="svc-shadow" style="left:863px"></div>

<div class="svc" style="left:113px">
  <div class="bubble">Lorem ipsum dolor sit amet, consectetuer adipiscing elit. Aenean commodo ligula eget dolor. Aenean massa. Cum sociis natoque penatibus et magnis</div>
  <svg class="icon" viewBox="0 0 54 50" aria-hidden="true"><rect x="9" y="10" width="36" height="24" fill="none" stroke="#f2505f" stroke-width="2.5"/><path d="M22 40 H32 M27 34 V40 M20 26 L32 16" stroke="#f2505f" stroke-width="2.5"/></svg>
  <div class="label"><em>.1</em>Full Stack Software<br>Development</div>
</div>
<div class="svc" style="left:362px">
  <div class="bubble">Lorem ipsum dolor sit amet, consectetuer adipiscing elit. Aenean commodo ligula eget dolor. Aenean massa. Cum sociis natoque penatibus et magnis</div>
  <svg class="icon" viewBox="0 0 54 50" aria-hidden="true"><rect x="14" y="6" width="26" height="36" fill="none" stroke="#f2505f" stroke-width="2.5"/><path d="M14 14 H40 M19 20 H35 M19 26 H35 M19 32 H29" stroke="#f2505f" stroke-width="2"/></svg>
  <div class="label"><em>.2</em>Website Design</div>
</div>
<div class="svc" style="left:612px">
  <div class="bubble">Lorem ipsum dolor sit amet, consectetuer adipiscing elit. Aenean commodo ligula eget dolor. Aenean massa. Cum sociis natoque penatibus et magnis</div>
  <svg class="icon" viewBox="0 0 54 50" aria-hidden="true"><rect x="17" y="13" width="20" height="20" fill="none" stroke="#f2505f" stroke-width="2.5"/><path d="M22 13 V5 M27 13 V5 M32 13 V5 M22 33 V41 M27 33 V41 M32 33 V41 M17 18 H8 M17 28 H8 M37 18 H46 M37 28 H46" stroke="#f2505f" stroke-width="2"/></svg>
  <div class="label"><em>.3</em>Fintech</div>
</div>
<div class="svc" style="left:863px">
  <div class="bubble">Lorem ipsum dolor sit amet, consectetuer adipiscing elit. Aenean commodo ligula eget dolor. Aenean massa. Cum sociis natoque penatibus et magnis</div>
  <svg class="icon" viewBox="0 0 54 50" aria-hidden="true"><g fill="none" stroke="#f2505f" stroke-width="2.5"><circle cx="27" cy="10" r="6"/><circle cx="14" cy="24" r="6"/><circle cx="40" cy="24" r="6"/><circle cx="27" cy="38" r="6"/></g></svg>
  <div class="label"><em>.4</em>Blockchain</div>
</div>

<div class="connector" style="top:1212px"></div>

<!-- banner -->
<div class="abs banner" role="img" aria-label="Dark blue banner over a photo of a business handshake">
  <h3>All of your favorite people</h3>
  <p>Welcome to connect with us!</p>
</div>
<div class="btn" style="left:753px;top:1354px;width:204px;height:48px;font-size:14px">CONTACT US NOW!</div>

<!-- projects -->
<div class="connector" style="top:1492px"></div>
<h2 class="abs heading" style="top:1558px">Our Projects</h2>
<div class="abs filters">
  <span>Show All</span><span>Full Stack Software Development</span><span>Website Design</span><span>Fintech</span><span>Blockchain</span>
</div>

<div class="photo" style="left:113px;top:1729px;width:237px;height:205px;background:linear-gradient(135deg,#9aa3ad,#d8d2c6)" role="img" aria-label="Hands holding a tablet with app icons floating above"></div>
<div class="photo" style="left:364px;top:1729px;width:239px;height:205px;background:linear-gradient(135deg,#cfc9c0,#e9e4dc)" role="img" aria-label="Office team working at computers"></div>
<div class="photo" style="left:617px;top:1729px;width:239px;height:205px;background:linear-gradient(135deg,#0f2236,#3e6c8c)" role="img" aria-label="Hand touching a glowing blockchain network graphic"></div>
<div class="photo" style="left:868px;top:1729px;width:219px;height:443px;background:linear-gradient(160deg,#d9dbd6,#b5c58a 55%,#e5e3df)" role="img" aria-label="Presenter pointing at a growth chart on a screen"></div>
<div class="photo" style="left:113px;top:1951px;width:237px;height:221px;background:linear-gradient(135deg,#c7c9c4,#eceae5)" role="img" aria-label="Team desk seen from above with laptops and fruit"></div>
<div class="photo" style="left:364px;top:1951px;width:492px;height:221px;background:linear-gradient(135deg,#d7cfc4,#eee9e1)" role="img" aria-label="Desk with laptop, notebooks and stationery seen from above"></div>

<div class="btn" style="left:516px;top:2199px;width:170px;height:51px;font-size:13px">
  <svg width="22" height="22" viewBox="0 0 22 22" aria-hidden="true"><g stroke="#fff" stroke-width="2" stroke-linecap="round"><path d="M11 2 V6"/><path d="M11 16 V20" opacity=".5"/><path d="M2 11 H6" opacity=".7"/><path d="M16 11 H20" opacity=".4"/><path d="M4.6 4.6 L7.4 7.4" opacity=".85"/><path d="M14.6 14.6 L17.4 17.4" opacity=".45"/><path d="M4.6 17.4 L7.4 14.6" opacity=".6"/><path d="M14.6 7.4 L17.4 4.6" opacity=".3"/></g></svg>
  LOAD MORE
</div>

<!-- testimonials -->
<div class="connector" style="top:2280px"></div>
<h2 class="abs heading" style="top:2347px">Client Testimonials</h2>
<div class="abs band"></div>
<svg class="abs" style="left:109px;top:2420px" width="440" height="440" aria-hidden="true">
  <circle cx="220" cy="220" r="216" fill="none" stroke="#ffffff" stroke-width="1.5"/>
  <circle cx="436" cy="220" r="6" fill="#ffffff"/>
</svg>
<div class="abs" style="left:127px;top:2438px;width:404px;height:404px;border-radius:50%;background:radial-gradient(circle at 50% 40%,#f08a2a,#d35b12 60%,#7a4b34)" role="img" aria-label="Photo of a client working on a laptop against an orange wall"></div>
<div class="abs quote">
  <p>&ldquo;Lorem ipsum dolor sit amet, consectetuer adipiscing elit. Aenean commodo ligula eget dolor. Aenean massa. Cum sociis natoque penatibus et magnis dis parturient montes, nascetur ridiculus mus. Donec quam felis, ultricies nec, pellentesque eu, pretium quis, sem. Nulla consequat massa quis enim. Donec pede justo, fringilla vel, aliquet nec, vulputate eget, arcu.</p>
  <p style="margin-top:12px">Lorem ipsum dolor sit amet, consectetuer adipiscing elit. Aenean commodo ligula eget dolor. Aenean massa.&rdquo;</p>
  <p class="who">- Aenean Vulputate</p>
  <p class="role">Eleifend Tellus</p>
</div>
<div class="abs tdots"><span class="on"></span><span></span><span></span></div>

<!-- blog -->
<div class="connector" style="top:2838px"></div>
<h2 class="abs heading" style="top:2906px">Latest Blog</h2>
<p class="abs lead">Lorem ipsum dolor sit amet, consectetuer adipiscing elit. Aenean commodo ligula eget dolor. Aenean massa. Lorem ipsum dolor sit amet</p>

<article class="post" style="left:113px">
  <div class="img" style="background:linear-gradient(135deg,#3a3f48,#d9d7d2)" role="img" aria-label="Business handshake over a desk"></div>
  <div class="date">12<br>Fab</div>
  <div class="title">CUM SOCIIS NATOQUE PENATIBUS</div>
  <div class="meta">By Admin &nbsp;&nbsp; Comments</div>
  <p class="excerpt">Lorem ipsum dolor sit amet, consectetuer adipiscing elit. Aenean commodo ligula eget dolor. Aenean massa. Cum sociis natoque</p>
</article>
<article class="post" style="left:450px">
  <div class="img" style="background:linear-gradient(135deg,#c9ccd4,#4a5a7a)" role="img" aria-label="Colleagues reviewing documents together"></div>
  <div class="date">12<br>Fab</div>
  <div class="title">CUM SOCIIS NATOQUE PENATIBUS</div>
  <div class="meta">By Admin &nbsp;&nbsp; Comments</div>
  <p class="excerpt">Lorem ipsum dolor sit amet, consectetuer adipiscing elit. Aenean commodo ligula eget dolor. Aenean massa. Cum sociis natoque</p>
</article>
<article class="post" style="left:787px">
  <div class="img" style="background:linear-gradient(135deg,#dfe6ee,#7d8fa8)" role="img" aria-label="Team members giving a high five by a window"></div>
  <div class="date">12<br>Fab</div>
  <div class="title">CUM SOCIIS NATOQUE PENATIBUS</div>
  <div class="meta">By Admin &nbsp;&nbsp; Comments</div>
  <p class="excerpt">Lorem ipsum dolor sit amet, consectetuer adipiscing elit. Aenean commodo ligula eget dolor. Aenean massa. Cum sociis natoque</p>
</article>

<div class="connector" style="top:3370px"></div>

<!-- contact -->
<div class="abs" style="left:0;top:3458px;width:1200px;height:477px;background:linear-gradient(120deg,#f1ece4,#efe2c8 60%,#f2ede4)" role="img" aria-label="Faded regional road map"></div>
<div class="abs contact-info">
  <h3>Contact Us</h3>
  <div class="row"><svg width="12" height="14" viewBox="0 0 12 14" aria-hidden="true"><path d="M6 0 C2.7 0 0 2.6 0 5.8 C0 10 6 14 6 14 C6 14 12 10 12 5.8 C12 2.6 9.3 0 6 0 Z" fill="#fff"/><circle cx="6" cy="5.8" r="2" fill="#1f2b4d"/></svg><span>Maple Court, Suite 12<br>04021</span></div>
  <div class="row"><svg width="12" height="12" viewBox="0 0 12 12" aria-hidden="true"><path d="M2 0 L4.5 3 L3 4.5 C4 6.5 5.5 8 7.5 9 L9 7.5 L12 10 L10 12 C4.5 11.5 0.5 7.5 0 2 Z" fill="#fff"/></svg><span>1800.555.0198</span></div>
  <div class="row"><svg width="12" height="12" viewBox="0 0 12 12" aria-hidden="true"><rect x="0" y="1" width="12" height="10" fill="#fff"/><rect x="2" y="3" width="8" height="2" fill="#1f2b4d"/></svg><span>1800.555.0198</span></div>
  <div class="row"><svg width="12" height="10" viewBox="0 0 12 10" aria-hidden="true"><rect width="12" height="10" fill="#fff"/><path d="M0 0 L6 5 L12 0" fill="none" stroke="#1f2b4d" stroke-width="1.2"/></svg><span>team@northgate.example</span></div>
</div>
<div class="abs contact-form">
  <h3>Get In Touch</h3>
  <p class="sub">Feel free to contact with us</p>
  <div class="field">Name:</div>
  <div class="field">Email:</div>
  <div class="field tall">Comments:</div>
  <div class="btn" style="position:relative;margin-top:16px;width:113px;height:36px;font-size:14px">Submit</div>
</div>

<!-- footer -->
<footer class="abs footer"></footer>
<div class="abs brand flogo"><span class="mark"></span>Northgate Tech Advisory</div>
<p class="abs fabout">Donec pede justo, fringilla vel, aliquet nec, vulputate eget, arcu. In enim justo, rhoncus ut, imperdiet a, venenatis vitae, justo. Donec pede justo, fringilla vel, aliquet nec</p>
<div class="abs fcol" style="left:510px">
  <h4>Quick Link</h4>
  <ul><li>Home</li><li>About Us</li><li>Services</li><li>Contact Us</li></ul>
</div>
<div class="abs fcol" style="left:674px">
  <h4>Services</h4>
  <ul><li>Stack Software Development</li><li>Website design</li><li>Fintech</li><li>Blockchain</li></ul>
</div>
<div class="abs fcol newsletter" style="left:886px">
  <h4>Newsletter</h4>
  <input type="text" placeholder="Enter your mail id:">
  <div class="btn" style="position:relative;width:105px;height:30px;font-size:13px">Subscribe</div>
</div>
<p class="abs copy">&copy; 2018 Northgate Tech Advisory . All rights reserved.</p>
<div class="abs fsocial"><span></span><span></span><span></span><span></span><span></span></div>

</body>
</html>
```